Website for Swedish wellness company "Heartmeadow"

We need a website for our Swedish wellness company. The name is "Heartmeadow" . The company is all about sustainablility for our body, soul and planet. We work with coaching, yoga, massage, healthy food, retreats(sports, excercise, sufing), healing and inspirational talks. We are convinced that personal sustainability and a strong spiritual connection to yourself will lead to planetary sustainability. Our customers are both companies and consumers from all over the world. The final design should be clean/simple and you should get a feeling of community, happiness, warmth, connection,, joy, spirituality but still a professional touch.Just got a logo from Pixel Forum and are very happy with it;-)
Updates

Sorry I was too enthusiastic posting this project. Of course I will give you some text as well för the different pages! I will see to that it is finished by friday so if you want to wait with your submissions please do! Best regards Maja

Target Market(s)

Businesses and consumers

Industry/Entity Type

Health And Wellness

Number of Pages Required

5+ page

Font styles to use
Sans Serif

Colors
33a6d7
00a990
b7a5cd

Requirements
Must have
• Idea about pages:
• I am not sure how many pages I get for the price, but 5 would be nice to start with.
• Not sure what write ups is;-)
• But title of the pages could be:
• Landing page
• About us
• Services
• Retreats
• Contact us
Nice to have
• A clean and professional website but with some heart and soul in it. Because we Would love colours that harmonize with our logo, but other ideas are welcome!

```html
<!DOCTYPE html>
<html lang="en">
<head>
<meta charset="utf-8">
<title>Heartmeadow</title>
<link href="https://fonts.googleapis.com/css2?family=Montserrat:wght@300;400;500&display=swap" rel="stylesheet">
<style>
:root{
  --navy:#123a6b;
  --teal:#4cc6c4;
  --bar:#eeeeef;
  --bar-text:#6f7377;
  --lilac-a:#b7a5cd;
  --lilac-b:#9f8fd8;
  --pink-a:#e06bc9;
  --pink-b:#b46ad8;
  --white:#ffffff;
}
*{margin:0;padding:0;box-sizing:border-box}
html,body{width:1200px;height:862px;overflow:hidden}
body{font-family:"Montserrat",sans-serif;position:relative;background:var(--white)}
.hero-photo{position:absolute;inset:0;
  background:
    linear-gradient(180deg,rgba(255,255,255,.95) 0%,rgba(255,255,255,.55) 14%,rgba(255,255,255,0) 30%),
    radial-gradient(circle at 62% 38%,#fff6ee 0%,rgba(255,230,215,.7) 12%,rgba(255,255,255,0) 30%),
    linear-gradient(180deg,#b9cfe4 0%,#d6e0ea 30%,#c9a989 55%,#d98aa6 68%,#7fd2d6 80%,#e4d6c8 92%,#6d6d72 100%);}
.topbar{position:absolute;top:0;left:492px;height:34px;display:flex;gap:2px;font-size:12px;color:var(--bar-text)}
.topbar>div{background:var(--bar);height:100%;display:flex;align-items:center;justify-content:center}
.follow{width:171px;color:var(--teal);gap:8px}
.follow span{margin-right:4px}
.dot{width:7px;height:7px;border-radius:50%;background:#8a8e92;display:inline-block;margin:0 3px}
.search{width:47px}
.call{width:174px}
.lang{width:121px;gap:8px}
.package{position:absolute;left:1015px;top:0;width:173px;height:60px;
  background:linear-gradient(180deg,var(--lilac-a),var(--lilac-b));
  color:#2e3550;font-size:13.5px;text-align:center;line-height:16px;padding-top:15px;letter-spacing:.2px}
.book{position:absolute;left:1015px;top:63px;width:173px;height:39px;border-radius:0 0 10px 10px;
  background:linear-gradient(180deg,var(--pink-a),var(--pink-b));color:var(--white);
  font-size:16px;display:flex;align-items:center;justify-content:center}
.nav{position:absolute;top:74px;left:0;font-size:14.5px;color:var(--navy)}
.nav a{position:absolute;white-space:nowrap;text-decoration:none;color:inherit}
.brand{position:absolute;left:41px;top:44px;width:190px;text-align:center}
.brand .mark{width:64px;height:64px;border-radius:50%;background:var(--teal);margin:0 auto 12px}
.brand .name{font-size:24px;font-weight:500;color:var(--navy);letter-spacing:.5px}
.headline{position:absolute;top:404px;left:0;width:1200px;text-align:center;color:var(--white);
  font-size:40px;font-weight:400;line-height:52px;letter-spacing:1px;text-shadow:0 1px 6px rgba(0,0,0,.35)}
.rule{position:absolute;top:525px;left:308px;width:584px;height:2px;background:var(--white)}
.tagline{position:absolute;top:549px;left:0;width:1200px;text-align:center;color:var(--navy);font-size:20px;
  text-shadow:0 0 6px rgba(255,255,255,.6)}
.scroll-cue{position:absolute;left:572px;top:610px}
</style>
</head>
<body>
<div class="hero-photo" role="img" aria-label="Rooftop pool terrace with tall palm trees under a bright cloudy sky and pink cabanas"></div>

<div class="topbar">
  <div class="follow"><span>Follow us on:</span><i class="dot"></i><i class="dot"></i><i class="dot"></i></div>
  <div class="search"><svg width="16" height="16" viewBox="0 0 16 16"><circle cx="6.5" cy="6.5" r="5" fill="none" stroke="#4cc6c4" stroke-width="1.8"/><line x1="10.2" y1="10.2" x2="14.5" y2="14.5" stroke="#4cc6c4" stroke-width="1.8"/></svg></div>
  <div class="call">Call: (855) 310-4827</div>
  <div class="lang">English <svg width="10" height="7" viewBox="0 0 10 7"><path d="M1 1l4 4 4-4" fill="none" stroke="#4cc6c4" stroke-width="1.8"/></svg></div>
</div>

<div class="package">SUMMER EXPERIENCE<br>
  <svg width="14" height="12" viewBox="0 0 14 12" style="vertical-align:-2px;margin-right:6px"><path d="M2 1l5 4 5-4M2 6l5 4 5-4" fill="none" stroke="#4cc6c4" stroke-width="1.8"/></svg>PACKAGE<svg width="14" height="12" viewBox="0 0 14 12" style="vertical-align:-2px;margin-left:12px"><path d="M2 1l5 4 5-4M2 6l5 4 5-4" fill="none" stroke="#4cc6c4" stroke-width="1.8"/></svg>
</div>
<div class="book">Book Your Stay</div>

<nav class="nav">
  <a style="left:495px">LOCATIONS</a>
  <a style="left:614px">DAILY SCHEDULE <svg width="10" height="7" viewBox="0 0 10 7"><path d="M1 1l4 4 4-4" fill="none" stroke="#4cc6c4" stroke-width="1.8"/></svg></a>
  <a style="left:780px">SHOP</a>
  <a style="left:857px">BLOG</a>
  <a style="left:933px">GALLERY</a>
</nav>

<div class="brand">
  <div class="mark"></div>
  <div class="name">HEARTMEADOW</div>
</div>

<h1 class="headline">SUSTAINABILITY FOR THE BODY, SOUL<br>AND PLANET IS OUR ULTIMATE GOAL</h1>
<div class="rule"></div>
<p class="tagline">We need to come back to balance</p>
<svg class="scroll-cue" width="56" height="54" viewBox="0 0 56 54"><path d="M0 0l28 28 28-28v26L28 54 0 26z" fill="#ffffff"/></svg>
</body>
</html>
```